Car Detailing product label for 750ML Clear Bottle

I need a label for various product with differente color for each products but in the same size bottle each time. It's only for our purpose no commercial application. I need a template with differente color but same design. The name for product it's : Brisk Harbor. We dont have any logo because it's only for us. We like like car silhouette in the logo or in background or something like that.

And for the product we have many like : APC Cleaner, Drying Aid, Wheel Cleaner and some other.

Font styles to use
Serif
Sans Serif

```html
<!DOCTYPE html>
<html lang="en">
<head>
<meta charset="utf-8">
<title>Brisk Harbor – APC Cleaner Label</title>
<link rel="stylesheet" href="https://fonts.googleapis.com/css2?family=Oswald:wght@300;500&family=Roboto:wght@700&display=swap">
<style>
  :root {
    --ink-black: #1b1b1c;
    --photo-light: #3a3b3f;
    --photo-dark: #121314;
    --silver: #d6d8dc;
    --silver-shade: #8e9095;
    --blue-light: #2f6fd0;
    --blue-mid: #2356b8;
    --blue-deep: #1a3a96;
    --white: #ffffff;
  }
  html, body {
    margin: 0;
    padding: 0;
    width: 1200px;
    height: 900px;
    overflow: hidden;
    background: #ffffff;
  }
  .label {
    position: relative;
    width: 1200px;
    height: 900px;
    overflow: hidden;
    background: var(--photo-dark);
  }
  .label-art {
    position: absolute;
    inset: 0;
    width: 1200px;
    height: 900px;
    display: block;
  }
  .brand-name {
    position: absolute;
    left: 0;
    width: 1200px;
    top: 46px;
    text-align: center;
    font-family: "Oswald", sans-serif;
    font-weight: 500;
    font-size: 54px;
    line-height: 52px;
    letter-spacing: 3px;
    color: var(--silver);
    text-transform: uppercase;
    margin: 0;
  }
  .product-name {
    position: absolute;
    left: 544px;
    top: 618px;
    margin: 0;
    font-family: "Oswald", sans-serif;
    text-transform: uppercase;
    color: var(--silver);
    line-height: 1;
  }
  .product-name .line-light {
    display: block;
    font-weight: 300;
    font-size: 96px;
    line-height: 78px;
    letter-spacing: 1px;
  }
  .product-name .line-bold {
    display: block;
    font-weight: 500;
    font-size: 96px;
    line-height: 82px;
    letter-spacing: 1px;
  }
  .volume {
    position: absolute;
    left: 744px;
    top: 836px;
    margin: 0;
    font-family: "Roboto", sans-serif;
    font-weight: 700;
    font-size: 31px;
    color: var(--white);
  }
</style>
</head>
<body>
<main class="label">
  <svg class="label-art" viewBox="0 0 1200 900" xmlns="http://www.w3.org/2000/svg">
    <defs>
      <linearGradient id="photo-tone" x1="0" y1="0" x2="1" y2="1">
        <stop offset="0" stop-color="var(--photo-light)"/>
        <stop offset="1" stop-color="var(--photo-dark)"/>
      </linearGradient>
      <linearGradient id="blue-panel" x1="1" y1="0" x2="0" y2="1">
        <stop offset="0" stop-color="var(--blue-light)"/>
        <stop offset="0.6" stop-color="var(--blue-mid)"/>
        <stop offset="1" stop-color="var(--blue-deep)"/>
      </linearGradient>
      <linearGradient id="silver-sweep" x1="0" y1="0" x2="1" y2="0">
        <stop offset="0" stop-color="var(--silver-shade)"/>
        <stop offset="0.5" stop-color="var(--silver)"/>
        <stop offset="1" stop-color="var(--silver-shade)"/>
      </linearGradient>
    </defs>

    <rect class="background-photo" x="0" y="0" width="1200" height="900" fill="url(#photo-tone)" role="img" aria-label="Photo of a dark sports car front on a carbon fibre texture"/>

    <path class="accent-stripe" d="M150 900 C330 590 690 330 1200 140 V175 C700 360 360 610 200 900 Z" fill="var(--blue-deep)"/>
    <path class="blue-panel" d="M205 900 C370 615 720 370 1200 190 V900 Z" fill="url(#blue-panel)"/>

    <path class="header-blue-line" d="M0 60 C170 150 400 215 600 215 C800 215 1020 150 1200 30 V48 C1020 170 800 226 600 226 C400 226 170 165 0 75 Z" fill="var(--blue-mid)"/>
    <path class="header-silver-line" d="M0 42 C170 130 400 196 600 196 C800 196 1020 130 1200 10 V34 C1020 156 800 214 600 214 C400 214 170 152 0 62 Z" fill="url(#silver-sweep)"/>
    <path class="header-band" d="M0 0 H1200 V12 C1020 128 800 182 600 182 C400 182 170 120 0 44 Z" fill="var(--ink-black)"/>
  </svg>

  <p class="brand-name">Brisk<br>Harbor</p>

  <h1 class="product-name">
    <span class="line-light">APC</span>
    <span class="line-bold">Cleaner</span>
  </h1>

  <p class="volume">750ml</p>
</main>
</body>
</html>
```